Business Card for a mobile physiotherapy company

I need a layout for a business card for a mobile physiotherapy company.
Slogan is "Mobile Physiotherapy - Your Road To Recovery"
Phone number is 867-402-5913
Email VantrePhysio@mailbright.ca (subject to change with website)
Website www.VantrePhysio.ca
My name and credentials: Kent Vantre Kent Vantre, BSc(kin), MPT, CAFCI, IMS
Information maybe included: Direct Billing, Services including Physiotherapy, IMS, acupuncture
Maybe include facebook and instagram logos
One side with the logo clean and sharp
Other side with details, try not to look too busy, keep everything concise

```html
<!DOCTYPE html>
<html lang="en">
<head>
<meta charset="utf-8">
<title>Vantre Therapy – Business Card</title>
<link rel="stylesheet" href="https://fonts.googleapis.com/css2?family=Lato:wght@400;700&display=swap">
<style>
  :root {
    --backdrop: #2b2b2d;
    --brand-green: #0d5b4e;
    --brand-green-dark: #0a4c41;
    --brand-navy: #26406f;
    --card-white: #ffffff;
    --ink: #1f2a2a;
    --soft-white: #e8f0ee;
  }
  * { box-sizing: border-box; margin: 0; padding: 0; }
  html, body {
    width: 1200px; height: 997px; overflow: hidden;
    background: var(--backdrop);
    font-family: "Lato", Arial, sans-serif;
  }
  .canvas { position: relative; width: 1200px; height: 997px; }

  .card {
    position: absolute; width: 560px; height: 320px;
    overflow: hidden; border-radius: 3px;
  }

  /* Front side */
  .card-front {
    left: 60px; top: 120px;
    background: var(--brand-green);
    color: var(--card-white);
  }
  .front-brand {
    position: absolute; left: 0; right: 0; top: 88px;
    display: flex; align-items: center; justify-content: center; gap: 14px;
  }
  .brand-mark {
    width: 18px; height: 18px; background: var(--card-white);
  }
  .brand-name {
    font-weight: 700; font-size: 38px; letter-spacing: 4px;
    text-transform: uppercase;
  }
  .front-rule {
    position: absolute; left: 36px; right: 36px; top: 214px;
    height: 1px; background: var(--soft-white); opacity: .8;
  }
  .services-title {
    position: absolute; left: 0; right: 0; top: 196px;
    text-align: center; font-size: 13px; font-weight: 700; letter-spacing: .5px;
  }
  .services-title span { background: var(--brand-green); padding: 0 10px; }
  .services-list {
    position: absolute; left: 0; right: 0; top: 228px;
    text-align: center; font-size: 13px; letter-spacing: .5px; color: var(--soft-white);
  }
  .front-base {
    position: absolute; left: 0; right: 0; bottom: 28px;
    height: 1px; background: var(--soft-white); opacity: .6;
  }

  /* Back side */
  .card-back {
    left: 580px; top: 500px;
    background: var(--card-white);
  }
  .back-wave { position: absolute; inset: 0; }
  .back-brand {
    position: absolute; left: 34px; top: 112px;
    display: flex; align-items: center; gap: 10px;
    color: var(--brand-green);
  }
  .back-brand .brand-mark { background: var(--brand-green); width: 14px; height: 14px; }
  .back-brand .brand-name { font-size: 28px; letter-spacing: 3px; }
  .holder {
    position: absolute; right: 26px; top: 30px; text-align: right;
  }
  .holder-name {
    color: var(--brand-green); font-weight: 700; font-size: 15px;
    text-transform: uppercase; letter-spacing: .5px;
  }
  .holder-credentials { color: var(--ink); font-size: 11px; margin-top: 3px; }
  .contacts {
    position: absolute; right: 24px; top: 178px;
    list-style: none; text-align: right; color: var(--card-white); font-size: 12px;
  }
  .contacts li {
    display: flex; justify-content: flex-end; align-items: center; gap: 7px;
    margin-bottom: 9px;
  }
  .contacts .web { font-weight: 700; }
  .contacts svg { width: 12px; height: 12px; flex: none; }
</style>
</head>
<body>
<main class="canvas">

  <section class="card card-front" aria-label="Card front">
    <div class="front-brand">
      <span class="brand-mark"></span>
      <span class="brand-name">Vantre Therapy</span>
    </div>
    <div class="front-rule"></div>
    <p class="services-title"><span>SERVICES INCLUDING</span></p>
    <p class="services-list">DIRECT BILLING, PHYSIOTHERAPY, IMS, ACUPUNCTURE</p>
    <div class="front-base"></div>
  </section>

  <section class="card card-back" aria-label="Card back">
    <svg class="back-wave" viewBox="0 0 560 320" width="560" height="320" aria-hidden="true">
      <path d="M0 262 C150 335 300 262 400 165 C460 110 515 100 560 108 L560 320 L0 320 Z" fill="var(--brand-green)"/>
      <path d="M0 246 C150 318 290 245 392 150 C455 92 515 80 560 90" fill="none" stroke="var(--brand-navy)" stroke-width="11"/>
    </svg>

    <div class="back-brand">
      <span class="brand-mark"></span>
      <span class="brand-name">Vantre Therapy</span>
    </div>

    <div class="holder">
      <p class="holder-name">Kent Vantre</p>
      <p class="holder-credentials">BSc(kin), MPT, CAFCI, IMS</p>
    </div>

    <ul class="contacts">
      <li>867-402-5913
        <svg viewBox="0 0 24 24"><path fill="#fff" d="M6.6 10.8a15 15 0 0 0 6.6 6.6l2.2-2.2a1 1 0 0 1 1-.25 11 11 0 0 0 3.6.6 1 1 0 0 1 1 1V20a1 1 0 0 1-1 1A17 17 0 0 1 3 4a1 1 0 0 1 1-1h3.5a1 1 0 0 1 1 1 11 11 0 0 0 .6 3.6 1 1 0 0 1-.25 1z"/></svg>
      </li>
      <li>VantrePhysio@mailbright.ca
        <svg viewBox="0 0 24 24"><rect x="2" y="5" width="20" height="14" rx="1" fill="#fff"/><path d="M2 6l10 7 10-7" fill="none" stroke="var(--brand-green)" stroke-width="2"/></svg>
      </li>
      <li class="web">www.VantrePhysio.ca
        <svg viewBox="0 0 24 24"><path d="M10 14a4 4 0 0 0 5.6 0l4-4a4 4 0 0 0-5.6-5.6l-1.2 1.2M14 10a4 4 0 0 0-5.6 0l-4 4a4 4 0 0 0 5.6 5.6l1.2-1.2" fill="none" stroke="#fff" stroke-width="2.4" stroke-linecap="round"/></svg>
      </li>
    </ul>
  </section>

</main>
</body>
</html>
```